Design 4 pages for an event discovery website

This is a contest for the design of 4 pages for an events discovery website. The feature is part of the new sign-up process.

Please see the attached document for a full scope, mockups and the parent category icons.

Target Market(s)

18-35 Australian event goers

Industry/Entity Type

Events

Number of Pages Required

4 page

```html
<!DOCTYPE html>
<html lang="en">
<head>
<meta charset="utf-8">
<title>Eventora – Sign Up</title>
<link rel="stylesheet" href="https://fonts.googleapis.com/css2?family=Titillium+Web:wght@400;600&family=Open+Sans:wght@400&display=swap">
<style>
  :root {
    --brand: #5068bf;
    --brand-dark: #2d3f8a;
    --ink: #111418;
    --field-border: #8a8f99;
    --field-error: #e4383c;
    --footer-bg: #151515;
    --footer-text: #f2f2f2;
    --panel: rgba(255,255,255,0.6);
    --hero-top: #e4e5ea;
    --hero-mid: #d6d9e2;
    --hero-bottom: #c9d1e4;
  }
  * { box-sizing: border-box; margin: 0; padding: 0; }
  html, body { width: 1200px; height: 831px; overflow: hidden; }
  body { position: relative; background: #fff; font-family: "Titillium Web", sans-serif; color: var(--ink); }

  .top-band { position: absolute; top: 0; left: 0; width: 1200px; height: 5px; background: var(--brand); }
  .account-tab { position: absolute; top: 4px; left: 968px; width: 118px; height: 27px; background: var(--brand);
    border-radius: 0 0 14px 14px; display: flex; align-items: center; justify-content: center; gap: 8px;
    color: #fff; font-size: 12px; font-weight: 600; }
  .account-tab .divider { width: 0; height: 16px; border-left: 1px dotted #fff; }

  .site-header { position: absolute; top: 5px; left: 0; width: 1200px; height: 119px; border-bottom: 1px solid #c9ccd2; }
  .brand-name { position: absolute; left: 97px; top: 35px; font-size: 40px; font-weight: 600; color: var(--brand); letter-spacing: 0.3px; }
  .main-nav { position: absolute; left: 752px; top: 54px; display: flex; gap: 45px; font-size: 17px; font-weight: 600; }
  .search-box { position: absolute; left: 909px; top: 45px; width: 191px; height: 36px; border: 1px solid #c8cbd1;
    border-radius: 3px; padding: 0 13px; display: flex; align-items: center; font-size: 15px; color: #6b6f76; }

  .hero { position: absolute; top: 124px; left: 0; width: 1200px; height: 582px; overflow: hidden; }
  .hero-photo { position: absolute; inset: 0;
    background: linear-gradient(180deg, var(--hero-top) 0%, var(--hero-mid) 60%, var(--hero-bottom) 100%); }
  .signup-panel { position: absolute; left: 97px; top: 0; width: 325px; height: 582px; background: var(--panel);
    border-left: 1px solid rgba(255,255,255,0.6); }
  .signup-title { position: absolute; left: 45px; top: 60px; font-size: 41px; font-weight: 600; line-height: 1; }
  .field { position: absolute; left: 45px; width: 236px; height: 39px; border: 1px solid var(--field-border); border-radius: 2px;
    background: rgba(255,255,255,0.15); padding: 0 17px; display: flex; align-items: center;
    font-family: "Open Sans", sans-serif; font-size: 12.5px; color: #555a62; }
  .field.is-invalid { border-color: var(--field-error); box-shadow: 0 0 2px rgba(228,56,60,0.6); }
  .signup-button { position: absolute; left: 46px; top: 481px; width: 234px; height: 44px; border-radius: 3px;
    background: linear-gradient(180deg, #5a6fc3, var(--brand-dark)); color: #fff; font-size: 16px; font-weight: 600;
    display: flex; align-items: center; justify-content: center; }

  .benefits { position: absolute; left: 480px; top: 147px; }
  .benefits h2 { font-size: 41px; font-weight: 600; color: var(--brand); line-height: 1; margin-bottom: 18px; }
  .benefits ul { list-style: none; }
  .benefits li { position: relative; padding-left: 15px; font-size: 15.6px; line-height: 34.3px; letter-spacing: 0.1px; }
  .benefits li::before { content: ""; position: absolute; left: 1px; top: 14px; width: 6px; height: 6px; background: #1b2450; transform: rotate(45deg); }

  .site-footer { position: absolute; top: 706px; left: 0; width: 1200px; height: 125px; background: var(--footer-bg); color: var(--footer-text); }
  .footer-nav { position: absolute; left: 98px; top: 36px; font-size: 13.8px; }
  .footer-nav span { margin: 0 5px; }
  .copyright { position: absolute; left: 98px; top: 70px; font-size: 13.5px; }
  .social-links { position: absolute; left: 944px; top: 50px; display: flex; gap: 16px; }
  .social-links span { width: 27px; height: 27px; display: block; }
  .social-links .s1 { background: #3b5998; }
  .social-links .s2 { background: #1b8dc0; }
  .social-links .s3 { background: #c9c9c9; }
  .social-links .s4 { background: #1a7ab8; }
</style>
</head>
<body>
  <div class="top-band"></div>
  <header class="site-header">
    <div class="brand-name">EVENTORA</div>
    <nav class="main-nav"><span>Find</span><span>Events</span></nav>
    <div class="search-box">Search</div>
  </header>
  <div class="account-tab"><span>Sign</span><span class="divider"></span><span>Login</span></div>

  <main class="hero">
    <div class="hero-photo" role="img" aria-label="Blurred background photo of people enjoying an event"></div>
    <section class="signup-panel">
      <h1 class="signup-title">Sign Up</h1>
      <div class="field is-invalid" style="top:133px">User Name</div>
      <div class="field" style="top:182px">Email Address</div>
      <div class="field" style="top:232px">Password</div>
      <div class="field" style="top:280px">Confirm Password</div>
      <div class="field" style="top:331px">First Name</div>
      <div class="field" style="top:379px">Last Name</div>
      <div class="field" style="top:427px">Date Of Birth</div>
      <div class="signup-button">SIGN UP NOW</div>
    </section>
    <section class="benefits">
      <h2>Benifits</h2>
      <ul>
        <li>Get personalised event recommendations</li>
        <li>Get notified about your favourite events - never miss out again</li>
        <li>Follow all your favourite artists, musicians, teams and players in one place</li>
        <li>Follow your favourite local venues to know everything happening there</li>
        <li>Get curated news and feature content on your favourite artists (coming soon)</li>
        <li>Invite your mates to events via Friendlink (FL sign-up only)</li>
      </ul>
    </section>
  </main>

  <footer class="site-footer">
    <div class="footer-nav">Find<span>/</span>Events<span>/</span>About Us<span>/</span>Search<span>/</span>Register<span>/</span>Contact Us</div>
    <div class="copyright">Copyrights © 2015 Brightwell Studio All Rights Reserved</div>
    <div class="social-links" aria-label="Social links">
      <span class="s1"></span><span class="s2"></span><span class="s3"></span><span class="s4"></span>
    </div>
  </footer>
</body>
</html>
```